VESKAR Social media ads

I to want develop a series of ads high tech looking as well as environmentally orientated to be used in social media. we build solar powered chemical injection pumps and compressors for oil the and gas industry. you may use our websites for more info as well as ask questions. i will include some pictures and a logo. i would like to run ads weekly and would like to see ideas on tasteful holiday messages, current event integration ideas and general consistant snappy casual engagement. i want to find someones unique style and work continuously with them.

Some possible slogans: Industrial Grade. Pecision Made.
- The enviromental approach to chemical injection
- VESKAR - Solar technology that pays you on your investment
- VESKAR- A smarter initial investment to achieve genius results
- VESKAR - Empowering Nature
- VESKAR solar power as nature intended it.
www.veskarpumps.example

Target Market(s)

Oil and Gas High Tech

Industry/Entity Type

Oil And Gas

Requirements
Must have
• HIGH TECH looking
• Enviromental themes
• Oil and gas Themes
Nice to have
• HD quality pics,
• moving pics
Should not have
• none

```html
<!DOCTYPE html>
<html lang="en">
<head>
<meta charset="utf-8">
<title>VESKAR – The environmental approach to chemical injection</title>
<link rel="stylesheet" href="https://fonts.googleapis.com/css2?family=Nunito:wght@800;900&family=Oswald:wght@500&display=swap">
<style>
  :root {
    --backdrop: #d9dbda;
    --banner: #ffffff;
    --green-dark: #00704a;
    --green-light: #8dc63f;
    --slate: #5b5b5b;
    --url-grey: #666666;
    --photo-deep: #14171a;
    --photo-mid: #3b4148;
  }
  html, body {
    margin: 0;
    padding: 0;
    width: 1200px;
    height: 1200px;
    overflow: hidden;
    background: var(--backdrop);
  }
  .canvas { display: block; width: 1200px; height: 1200px; }
  .banner-bg { fill: var(--banner); stroke: #e4e4e4; stroke-width: 1; }
  .dash-dark { fill: var(--green-dark); }
  .dash-light { fill: var(--green-light); }
  .brand-name {
    font-family: "Nunito", sans-serif;
    font-weight: 900;
    font-size: 50px;
    fill: var(--green-dark);
  }
  .brand-dot { fill: var(--green-dark); }
  .headline-box-top { fill: var(--slate); }
  .headline-box-mid { fill: var(--green-dark); }
  .headline-box-low { fill: var(--green-light); }
  .headline {
    font-family: "Nunito", sans-serif;
    font-weight: 900;
    fill: #ffffff;
  }
  .headline-line-1 { font-size: 43px; }
  .headline-line-2 { font-size: 42px; }
  .headline-line-3 {
    font-family: "Oswald", sans-serif;
    font-weight: 500;
    font-size: 46px;
  }
  .site-url {
    font-family: "Nunito", sans-serif;
    font-weight: 800;
    font-size: 21px;
    fill: var(--url-grey);
  }
  .stripe-dark { fill: var(--green-dark); }
  .stripe-light { fill: var(--green-light); }
  .badge-ring { fill: var(--green-light); }
  .badge-inner { fill: #ffffff; }
  .badge-core { fill: var(--green-dark); }
</style>
</head>
<body>
<svg class="canvas" viewBox="0 0 1500 1500" xmlns="http://www.w3.org/2000/svg">
  <defs>
    <linearGradient id="pumpPhotoTone" x1="0" y1="0" x2="0.4" y2="1">
      <stop offset="0" stop-color="#14171a"/>
      <stop offset="0.55" stop-color="#3b4148"/>
      <stop offset="1" stop-color="#14171a"/>
    </linearGradient>
  </defs>

  <rect class="banner-bg" x="5" y="450" width="1490" height="600"/>

  <!-- slanted photo frame -->
  <polygon class="stripe-light" points="52,1050 182,450 215,450 85,1050"/>
  <polygon class="stripe-dark" points="85,1050 215,450 245,450 118,1050"/>
  <polygon role="img" aria-label="Photo of a solar powered chemical injection pump with stainless tubing, valves and plungers on a skid"
           fill="url(#pumpPhotoTone)" points="118,1050 245,450 770,450 640,1050"/>
  <polygon class="stripe-dark" points="640,1050 770,450 800,450 670,1050"/>
  <polygon class="stripe-light" points="670,1050 800,450 830,450 700,1050"/>

  <!-- round badge on frame edge -->
  <circle class="badge-ring" cx="730" cy="740" r="88"/>
  <circle class="badge-inner" cx="730" cy="740" r="80"/>
  <circle class="badge-core" cx="730" cy="740" r="72"/>

  <!-- decorative dashes -->
  <rect class="dash-light" x="52" y="485" width="36" height="6"/>
  <rect class="dash-dark" x="52" y="541" width="114" height="8"/>
  <rect class="dash-dark" x="26" y="557" width="114" height="8"/>
  <rect class="dash-dark" x="891" y="491" width="180" height="9"/>
  <rect class="dash-dark" x="844" y="513" width="114" height="9"/>
  <rect class="dash-dark" x="741" y="1012" width="115" height="9"/>
  <rect class="dash-dark" x="1000" y="655" width="254" height="7"/>
  <rect class="dash-dark" x="1265" y="655" width="13" height="7"/>
  <rect class="dash-dark" x="976" y="673" width="360" height="8"/>
  <rect class="dash-light" x="1405" y="688" width="6" height="80"/>
  <rect class="dash-dark" x="1383" y="790" width="7" height="90"/>
  <rect class="dash-dark" x="976" y="818" width="6" height="90"/>
  <rect class="dash-light" x="997" y="914" width="223" height="7"/>
  <rect class="dash-light" x="1063" y="936" width="224" height="7"/>
  <rect class="dash-light" x="1301" y="936" width="36" height="7"/>

  <!-- brand name -->
  <g class="brand">
    <circle class="brand-dot" cx="1032" cy="575" r="22"/>
    <text class="brand-name" x="1066" y="593">VESKAR</text>
  </g>

  <!-- headline -->
  <g class="headline-group">
    <rect class="headline-box-top" x="977" y="694" width="414" height="84"/>
    <text class="headline headline-line-1" x="1184" y="752" text-anchor="middle" textLength="390" lengthAdjust="spacingAndGlyphs">The environmental</text>
    <rect class="headline-box-mid" x="995" y="781" width="379" height="62"/>
    <text class="headline headline-line-2" x="1184" y="824" text-anchor="middle">approach to</text>
    <rect class="headline-box-low" x="1013" y="853" width="343" height="53"/>
    <text class="headline headline-line-3" x="1184" y="899" text-anchor="middle" textLength="300" lengthAdjust="spacingAndGlyphs">CHEMICAL INJECTION</text>
  </g>

  <text class="site-url" x="1457" y="1019" text-anchor="end">www.veskarpumps.example</text>
</svg>
</body>
</html>
```